Web Design for a company in Oil & Gas Business

We need a web design for our company based in Sydney called "Harbourline Meridian Supply". Main core of business are Engineering and Procurement services for Oil, Gas and Petrochemical Industry. It is important to highlight both capabilities in the website. Engineering services focuses on Technology Transfer, Know-how consultation as well as Detail Engineering. Regarding Procurement services, we provide full services starting from Offering, Order finalisation, Logistic coordination up to financial settlement of the project. Our Logo is combination of dark blue and Red. It is also important that the website would be compatible to various devices (mobile, tablet, PC).
Reason: I would like to receive more design ideas.
Business
1 page

```html
<!DOCTYPE html>
<html lang="en">
<head>
<meta charset="utf-8">
<title>Harbourline Meridian Supply</title>
<link href="https://fonts.googleapis.com/css2?family=Open+Sans:wght@300;400;600&family=Oswald:wght@600&family=Arimo&display=swap" rel="stylesheet">
<style>
:root{
  --navy:#0e2a6b;
  --red:#d3202b;
  --ink:#222;
  --grey-text:#8a8a8a;
  --soft:#f3f3f3;
  --footer:#2f2f2f;
  --footer-text:#9a9a9a;
  --black-btn:#1b1b1b;
}
*{box-sizing:border-box;margin:0;padding:0}
html,body{width:783px;height:1200px;overflow:hidden}
body{font-family:"Open Sans",sans-serif;color:var(--ink);background:#fff;position:relative}
.abs{position:absolute}

.site-header{left:0;top:0;width:783px;height:72px;background:linear-gradient(#f9f9f9,#e9e9e9);border-bottom:1px solid #ddd}
.brand{left:70px;top:24px;display:flex;align-items:center;gap:8px}
.brand-mark{width:22px;height:22px;border-radius:50%;background:var(--navy)}
.brand-name{font-size:14px;font-weight:600;color:var(--navy);line-height:1}
.social-top{left:483px;top:24px;display:flex;gap:4px}
.social-top span{width:21px;height:21px;border-radius:50%;background:#fff;border:1px solid #ccc;box-shadow:0 1px 2px rgba(0,0,0,.15)}
.call-btn{left:619px;top:23px;width:89px;height:26px;border-radius:4px 13px 13px 4px;background:var(--black-btn);color:#fff;font-size:12px;display:flex;align-items:center;justify-content:center}

.main-nav{left:0;top:72px;width:783px;height:36px;background:#fff;font-size:8.5px;color:#333}
.main-nav a{position:absolute;top:14px;color:#333;text-decoration:none}
.nav-mark{left:70px;top:71px;width:42px;height:1px;background:var(--red)}

.hero{left:0;top:108px;width:783px;height:240px;background:
  linear-gradient(90deg,rgba(120,70,40,.2),rgba(0,0,0,0) 55%),
  linear-gradient(180deg,#9c8f8c 0%,#c7a8a0 35%,#c98a6b 65%,#8b6c5c 90%,#a0a6ac 100%)}
.hero-title{left:434px;top:143px;font-size:27px;line-height:27px;color:#111;font-weight:400}
.hero-copy{left:435px;top:209px;width:250px;font-size:9.5px;line-height:12.5px;color:#fff;font-weight:300}
.red-btn{left:436px;top:256px;width:72px;height:25px;border-radius:13px;background:var(--red);color:#fff;font-size:8px;display:flex;align-items:center;justify-content:center}

.intro{left:0;top:348px;width:783px;height:116px;background:var(--soft);border-bottom:1px solid #e2e2e2}
.intro-text{left:79px;top:22px;width:640px;font-size:11.3px;line-height:17px;color:#333;font-weight:300}
.intro-text strong{font-family:"Oswald",sans-serif;color:var(--navy);font-size:14px;letter-spacing:-.2px;margin-right:12px;font-weight:600}
.dark-btn{height:25px;background:var(--black-btn);color:#fff;font-size:8.5px;font-weight:600;display:flex;align-items:center;justify-content:center;border-radius:2px}

.industry{width:185px;height:80px}
.industry-icon{width:26px;height:26px;border-radius:50%;background:#1d1d1d;position:absolute;left:0;top:0}
.industry-title{position:absolute;left:34px;top:4px;font-size:10px;color:#222;white-space:nowrap}
.industry-rule{position:absolute;left:34px;top:22px;width:150px;height:1px;background:#e4e4e4}
.industry-rule::before{content:"";position:absolute;left:0;top:0;width:42px;height:1px;background:var(--red)}
.industry-text{position:absolute;left:35px;top:33px;width:142px;font-size:7.6px;line-height:9.7px;color:var(--grey-text)}
.view-all{left:629px;top:686px;font-size:8.5px;color:var(--red);font-style:italic;text-decoration:underline}
.pager{top:686px;width:11px;height:11px;background:#eee;border:1px solid #ddd}

.services{left:0;top:712px;width:783px;height:232px;background:var(--soft)}
.card-image{top:25px;width:197px;height:98px}
.card-title{top:128px;font-size:10px;font-weight:400;color:#222}
.card-text{top:150px;width:186px;font-size:7.6px;line-height:9.3px;color:var(--grey-text)}
.small-btn{top:199px;width:55px;height:19px;border-radius:4px 10px 10px 4px;background:var(--black-btn);color:#fff;font-size:6px;display:flex;align-items:center;justify-content:center}

.partners{left:0;top:944px;width:783px;height:100px;background:#fff}
.badge{top:26px;height:48px;background:#9a9a9a;opacity:.85}

.site-footer{left:0;top:1044px;width:783px;height:156px;background:var(--footer);border-top:3px solid #555}
.col-title{font-size:10px;color:#fff;font-weight:600}
.col-list{font-size:7.5px;line-height:11.8px;color:var(--footer-text)}
.newsletter{left:539px;top:38px;width:166px;height:23px;background:#fff;border:1px solid #ccc;font-size:6.5px;font-style:italic;color:#aaa;padding:6px 9px}
.foot-social{left:539px;top:72px;display:flex;gap:5px}
.foot-social span{width:16px;height:16px;border-radius:2px}
.foot-rule{left:80px;top:120px;width:623px;height:1px;background:#444}
.copyright{left:0;top:130px;width:783px;text-align:center;font-family:"Arimo",sans-serif;font-size:10px;color:#fff}
</style>
</head>
<body>

<header class="site-header abs">
  <div class="brand abs"><span class="brand-mark"></span><span class="brand-name">Harbourline Meridian Supply</span></div>
  <div class="social-top abs"><span></span><span></span><span></span><span></span><span></span></div>
  <div class="call-btn abs">Call Today</div>
</header>
<div class="nav-mark abs"></div>

<nav class="main-nav abs">
  <a style="left:79px">Home</a>
  <a style="left:129px">Services</a>
  <a style="left:188px">Benefits</a>
  <a style="left:247px">Management</a>
  <a style="left:326px">Planning</a>
  <a style="left:387px">Optimization</a>
  <a style="left:464px">Industry</a>
  <a style="left:523px">Software</a>
  <a style="left:585px">Contact Us</a>
  <a style="left:654px">Recruitment</a>
</nav>

<section class="hero abs" role="img" aria-label="Photograph of a petrochemical refinery with towers and smoke under a warm sky"></section>
<h1 class="hero-title abs">Engineering &amp;<br>Procurement Services</h1>
<p class="hero-copy abs">Technology transfer, know-how consultation and detail engineering, backed by procurement from offering through to final settlement</p>
<div class="red-btn abs">Read More</div>

<section class="intro abs">
  <p class="intro-text abs"><strong>HARBOURLINE MERIDIAN SUPPLY</strong>Sydney-based engineering and procurement services for Oil, Gas and Petrochemical projects, from technology transfer and detail engineering to logistics and final settlement.</p>
  <div class="dark-btn abs" style="left:296px;top:66px;width:82px">SEE FEATURES</div>
  <div class="dark-btn abs" style="left:382px;top:66px;width:94px">CONTACT US</div>
</section>

<section class="capabilities">
  <div class="industry abs" style="left:77px;top:497px"><span class="industry-icon"><svg width="26" height="26"><g fill="#fff"><rect x="7" y="13" width="3" height="6"/><rect x="11" y="9" width="3" height="10"/><rect x="15" y="11" width="3" height="8"/></g></svg></span><span class="industry-title">Technology Transfer</span><span class="industry-rule"></span><p class="industry-text">Licensed process technology moved safely into your plant, with training and start-up support from our engineers.</p></div>
  <div class="industry abs" style="left:300px;top:497px"><span class="industry-icon"><svg width="26" height="26"><rect x="8" y="8" width="10" height="11" fill="none" stroke="#fff" stroke-width="1.5"/></svg></span><span class="industry-title">Know-how Consultation</span><span class="industry-rule"></span><p class="industry-text">Practical advice on process, equipment and operations drawn from years of oil, gas and petrochemical work.</p></div>
  <div class="industry abs" style="left:524px;top:497px"><span class="industry-icon"><svg width="26" height="26"><rect x="8" y="7" width="10" height="12" fill="#fff"/><g fill="#1d1d1d"><rect x="10" y="9" width="2" height="2"/><rect x="14" y="9" width="2" height="2"/><rect x="10" y="13" width="2" height="2"/><rect x="14" y="13" width="2" height="2"/></g></svg></span><span class="industry-title">Detail Engineering</span><span class="industry-rule"></span><p class="industry-text">Complete drawings, specifications and data sheets ready for purchasing, fabrication and construction.</p></div>

  <div class="industry abs" style="left:77px;top:594px"><span class="industry-icon"><svg width="26" height="26"><path d="M7 11q6-5 12 0l-2 2-2-1h-4l-2 1z" fill="#fff"/><rect x="9" y="14" width="8" height="5" fill="var(--red)"/></svg></span><span class="industry-title">Offering &amp; Ordering</span><span class="industry-rule"></span><p class="industry-text">Competitive offers from trusted vendors, clear evaluation and order finalisation on agreed terms.</p></div>
  <div class="industry abs" style="left:300px;top:594px"><span class="industry-icon"><svg width="26" height="26"><path d="M7 19V8h2v6l3-2v2l3-2v2l3-2v7z" fill="#fff"/></svg></span><span class="industry-title">Logistic Coordination</span><span class="industry-rule"></span><p class="industry-text">Expediting, inspection, shipping and customs handled so equipment reaches site on schedule.</p></div>
  <div class="industry abs" style="left:524px;top:594px"><span class="industry-icon"><svg width="26" height="26"><rect x="12" y="6" width="7" height="3" fill="var(--red)"/><path d="M7 19v-8h5v-2h2v10z" fill="#fff"/><rect x="14" y="13" width="5" height="6" fill="#fff"/></svg></span><span class="industry-title">Financial Settlement</span><span class="industry-rule"></span><p class="industry-text">Invoicing, payments and close-out managed through to the final financial settlement of the project.</p></div>

  <span class="view-all abs">View all</span>
  <span class="pager abs" style="left:669px"></span>
  <span class="pager abs" style="left:682px"></span>
</section>

<section class="services abs">
  <div class="card-image abs" style="left:84px;background:linear-gradient(#4f86c4 0%,#8fb3d6 55%,#7a7a3e 60%,#6d6b34 100%)" role="img" aria-label="Photograph of an oil pump jack on open grassland"></div>
  <h3 class="card-title abs" style="left:85px">Engineering Services</h3>
  <p class="card-text abs" style="left:86px">Technology transfer, know-how consultation and detail engineering delivered by one team, from early concept to construction-ready design.</p>
  <div class="small-btn abs" style="left:86px">Read More</div>

  <div class="card-image abs" style="left:293px;background:linear-gradient(#cfd4d8 0%,#9aa0a4 40%,#7e7e72 60%,#c9c9c2 100%)" role="img" aria-label="Photograph of pipelines leading to a refinery"></div>
  <h3 class="card-title abs" style="left:295px">Procurement Services</h3>
  <p class="card-text abs" style="left:296px">Full-cycle procurement, from offering and order finalisation to logistic coordination and the financial settlement of each project.</p>
  <div class="small-btn abs" style="left:296px">Read More</div>

  <div class="card-image abs" style="left:501px;background:linear-gradient(135deg,#1d4f8a,#4e94c8 45%,#1a3f6e 75%,#3a78b0)" role="img" aria-label="Photograph of blue-lit industrial pipework"></div>
  <h3 class="card-title abs" style="left:504px">Oil, Gas &amp; Petrochemical</h3>
  <p class="card-text abs" style="left:505px">Serving operators and contractors across Australia and overseas, for large multinational companies and smaller privately owned businesses.</p>
  <div class="small-btn abs" style="left:506px">Read More</div>
</section>

<section class="partners abs" aria-label="Partners">
  <span class="badge abs" style="left:97px;width:54px;border-radius:50%"></span>
  <span class="badge abs" style="left:186px;width:60px;border-radius:3px"></span>
  <span class="badge abs" style="left:290px;width:68px;border-radius:3px"></span>
  <span class="badge abs" style="left:405px;width:76px;border-radius:3px"></span>
  <span class="badge abs" style="left:513px;width:68px;border-radius:3px"></span>
  <span class="badge abs" style="left:615px;width:66px;border-radius:50%"></span>
</section>

<footer class="site-footer abs">
  <h4 class="col-title abs" style="left:80px;top:20px">Links</h4>
  <p class="col-list abs" style="left:80px;top:40px">Home<br>About Us<br>Benefits<br>Management</p>
  <h4 class="col-title abs" style="left:197px;top:21px">About Us</h4>
  <p class="col-list abs" style="left:195px;top:39px">Oil &amp; Gas<br>Telecommunicatios<br>New Industries</p>
  <h4 class="col-title abs" style="left:320px;top:21px">Connect with us</h4>
  <p class="col-list abs" style="left:320px;top:39px"><span style="font-size:9px">harbourlinemeridian.example</span><br>+61 0400 555 018</p>
  <h4 class="col-title abs" style="left:539px;top:21px">Sign up for newsletter</h4>
  <div class="newsletter abs">Enter Your Email Address</div>
  <div class="foot-social abs"><span style="background:#3a8ed8"></span><span style="background:#3b5aa0"></span><span style="background:#c8302a"></span><span style="background:#d94a35"></span></div>
  <div class="foot-rule abs"></div>
  <p class="copyright abs">©2015 harbourlinemeridian.example, All right reserved</p>
</footer>

</body>
</html>
```